New "above the fold" design for our website

We would like to see some new creative designs for our above the fold section on our homepage. We are an online marketplace for fresh produce and meat.

You must design the desktop and mobile layouts.

Target Market(s)

Women 30-45 years old who buy groceries, with 2 children under 10 years old.

Industry/Entity Type

Grocery Store

Number of Pages Required

1 page

Font styles to use
Sans Serif

Requirements
Must have
• Give customers the sense of organic and farm fresh as we are battling the big supermarket chains.
Nice to have
• Pictures of produce. Pictures of farmers.

```html
<!DOCTYPE html>
<html lang="en">
<head>
<meta charset="utf-8">
<title>Fieldhand – Quality Meat &amp; Produce</title>
<link href="https://fonts.googleapis.com/css2?family=Roboto+Condensed:wght@400;700&family=Roboto:wght@400;500&family=Open+Sans:wght@400&display=swap" rel="stylesheet">
<style>
  :root {
    --green: #566b2b;
    --green-light: #6f8540;
    --green-border: #8ea35c;
    --ink: #222222;
    --muted: #555555;
    --footer: #262626;
    --footer-text: #cfcfcf;
    --white: #ffffff;
  }
  * { box-sizing: border-box; margin: 0; padding: 0; }
  html, body { width: 979px; height: 1200px; overflow: hidden; background: var(--white); }
  body { position: relative; font-family: "Open Sans", sans-serif; color: var(--ink); }

  .hero { position: absolute; left: 0; top: 0; width: 979px; height: 522px; overflow: hidden; }
  .hero-photo {
    position: absolute; inset: 0;
    background: linear-gradient(180deg, #6f7f8c 0%, #8d9aa0 30%, #6f8a4e 48%, #4f6e34 75%, #3d5a2a 100%);
  }
  .hero-shade { position: absolute; inset: 0; background: rgba(20, 28, 20, 0.25); }

  .brand {
    position: absolute; left: 80px; top: 44px;
    font-family: "Roboto Condensed", sans-serif; font-weight: 700;
    font-size: 24px; letter-spacing: 2px; color: var(--white);
  }

  .nav { position: absolute; top: 54px; left: 0; width: 979px; height: 27px; font-family: "Roboto", sans-serif; font-size: 12px; color: var(--white); }
  .nav a { position: absolute; top: 0; line-height: 27px; color: var(--white); text-decoration: none; text-transform: uppercase; }
  .nav .btn { text-align: center; height: 27px; border: 1px solid rgba(255,255,255,0.85); }
  .nav .btn-login { left: 726px; width: 98px; background: rgba(0,0,0,0.1); }
  .nav .btn-register { left: 810px; width: 88px; background: var(--green); border-color: var(--green-border); }

  .headline {
    position: absolute; top: 228px; left: 0; width: 979px; text-align: center;
    font-family: "Roboto Condensed", sans-serif; font-weight: 700; font-size: 42px; color: var(--white);
    letter-spacing: 0.5px;
  }
  .subline {
    position: absolute; top: 280px; left: 0; width: 979px; text-align: center;
    font-family: "Roboto", sans-serif; font-size: 24px; color: var(--white); letter-spacing: 0.5px;
  }
  .search { position: absolute; left: 203px; top: 338px; width: 341px; height: 37px; background: var(--white); text-align: center; line-height: 37px; font-family: "Roboto", sans-serif; font-size: 16px; color: #333; }
  .shop-now { position: absolute; left: 554px; top: 337px; width: 222px; height: 38px; background: var(--green); border: 1px solid var(--green-border); text-align: center; line-height: 36px; font-family: "Roboto", sans-serif; font-size: 14px; color: var(--white); }

  .slide-arrow { position: absolute; top: 274px; width: 28px; height: 28px; }
  .slide-arrow.prev { left: 26px; }
  .slide-arrow.next { left: 922px; }

  .stats { position: absolute; top: 560px; left: 0; width: 979px; height: 80px; }
  .stat { position: absolute; top: 0; width: 154px; height: 80px; }
  .stat svg.frame { position: absolute; inset: 0; }
  .stat .icon { position: absolute; left: 65px; top: 15px; width: 24px; height: 24px; }
  .stat .label { position: absolute; left: 0; top: 47px; width: 154px; text-align: center; font-family: "Roboto Condensed", sans-serif; font-size: 13px; color: var(--white); }

  .welcome { position: absolute; top: 674px; left: 0; width: 979px; text-align: center; font-family: "Roboto", sans-serif; font-size: 30px; color: var(--ink); }
  .welcome span { color: var(--green); }
  .intro { position: absolute; top: 720px; left: 130px; width: 719px; text-align: center; font-size: 9.4px; line-height: 17px; color: var(--muted); }

  .card { position: absolute; top: 806px; width: 258px; }
  .card-title { height: 40px; background: var(--green-light); color: var(--white); text-align: center; line-height: 40px; font-family: "Roboto", sans-serif; font-size: 17px; }
  .card-photo { margin-top: 5px; height: 136px; }
  .photo-organic { background: linear-gradient(135deg, #a8c24a 0%, #4f7a2a 45%, #d9a63a 75%, #c9a24a 100%); }
  .photo-farm { background: linear-gradient(160deg, #c9d6e0 0%, #6d9a3e 40%, #e08a2a 65%, #4f7a2a 100%); }
  .photo-meat { background: linear-gradient(140deg, #b8384a 0%, #d05a5a 35%, #5c9a3a 55%, #8a2a3a 100%); }
  .card-text { margin-top: 21px; text-align: center; font-size: 9.4px; line-height: 17px; color: var(--muted); padding: 0 6px; }

  .footer { position: absolute; left: 0; top: 1094px; width: 979px; height: 106px; background: var(--footer); color: var(--footer-text); }
  .footer h3 { position: absolute; font-family: "Roboto", sans-serif; font-weight: 400; font-size: 15px; color: #e6e6e6; }
  .footer p { position: absolute; font-size: 10px; }
  .copy-head { left: 83px; top: 29px; }
  .copy-text { left: 83px; top: 50px; }
  .footer-links { left: 82px; top: 70px; font-size: 11px !important; }
  .addr-head { left: 433px; top: 29px; }
  .addr-text { left: 433px; top: 50px; }
  .addr-phone { left: 433px; top: 68px; }
  .follow-head { left: 732px; top: 37px; }
  .social { position: absolute; top: 38px; width: 20px; height: 20px; background: #f2f2f2; border-radius: 3px; }
</style>
</head>
<body>

<header class="hero">
  <div class="hero-photo" role="img" aria-label="Farmer holding a tablet in a pasture with grazing dairy cows"></div>
  <div class="hero-shade"></div>

  <div class="brand">FIELDHAND</div>

  <nav class="nav">
    <a style="left:452px">Home</a>
    <a style="left:526px">About Us</a>
    <a style="left:621px">How It Works</a>
    <a class="btn btn-login">Login</a>
    <a class="btn btn-register">Register</a>
  </nav>

  <h1 class="headline">QUALITY MEAT &amp; PRODUCE</h1>
  <p class="subline">DELIVERED TO YOUR DOOR</p>

  <div class="search">2010</div>
  <div class="shop-now">SHOP NOW</div>

  <svg class="slide-arrow prev" viewBox="0 0 28 28"><circle cx="14" cy="14" r="13" fill="rgba(0,0,0,0.35)" stroke="rgba(255,255,255,0.4)"/><path d="M16 8 L10 14 L16 20" fill="none" stroke="#fff" stroke-width="1.6"/></svg>
  <svg class="slide-arrow next" viewBox="0 0 28 28"><circle cx="14" cy="14" r="13" fill="rgba(0,0,0,0.35)" stroke="rgba(255,255,255,0.4)"/><path d="M12 8 L18 14 L12 20" fill="none" stroke="#fff" stroke-width="1.6"/></svg>
</header>

<section class="stats">
  <div class="stat" style="left:168px">
    <svg class="frame" viewBox="0 0 154 80"><polygon points="12,8 77,1 142,8 152,18 152,62 142,72 77,79 12,72 2,62 2,18" fill="var(--green)" stroke="var(--green)" stroke-width="2"/><polygon points="14,11 77,5 140,11 148,20 148,60 140,69 77,75 14,69 6,60 6,20" fill="none" stroke="var(--green-border)" stroke-width="1"/></svg>
    <svg class="icon" viewBox="0 0 24 24"><path d="M5 2 H15 L20 7 V22 H5 Z" fill="#fff"/><path d="M8 11 H17 M8 14 H17 M8 17 H17" stroke="var(--green)" stroke-width="1.4"/></svg>
    <div class="label">34482 ORDERS</div>
  </div>
  <div class="stat" style="left:336px">
    <svg class="frame" viewBox="0 0 154 80"><polygon points="12,8 77,1 142,8 152,18 152,62 142,72 77,79 12,72 2,62 2,18" fill="var(--green)" stroke="var(--green)" stroke-width="2"/><polygon points="14,11 77,5 140,11 148,20 148,60 140,69 77,75 14,69 6,60 6,20" fill="none" stroke="var(--green-border)" stroke-width="1"/></svg>
    <svg class="icon" viewBox="0 0 24 24" fill="#fff"><circle cx="12" cy="7" r="4"/><circle cx="5" cy="9" r="3"/><circle cx="19" cy="9" r="3"/><path d="M5 22 C5 14 19 14 19 22 Z"/><path d="M0 19 C0 13 7 13 7 16 V19 Z M24 19 C24 13 17 13 17 16 V19 Z"/></svg>
    <div class="label">10088 CUSTOMERS</div>
  </div>
  <div class="stat" style="left:497px">
    <svg class="frame" viewBox="0 0 154 80"><polygon points="12,8 77,1 142,8 152,18 152,62 142,72 77,79 12,72 2,62 2,18" fill="var(--green)" stroke="var(--green)" stroke-width="2"/><polygon points="14,11 77,5 140,11 148,20 148,60 140,69 77,75 14,69 6,60 6,20" fill="none" stroke="var(--green-border)" stroke-width="1"/></svg>
    <svg class="icon" viewBox="0 0 24 24"><path d="M3 10 H7 V21 H3 Z M9 10 L13 2 C15 2 15 4 14.5 6 L14 9 H20 C21.5 9 22 10 21.5 11.5 L19 20 C18.7 21 18 21 17 21 H9 Z" fill="none" stroke="#fff" stroke-width="1.6" stroke-linejoin="round"/></svg>
    <div class="label">10279 LIKES</div>
  </div>
  <div class="stat" style="left:658px">
    <svg class="frame" viewBox="0 0 154 80"><polygon points="12,8 77,1 142,8 152,18 152,62 142,72 77,79 12,72 2,62 2,18" fill="var(--green)" stroke="var(--green)" stroke-width="2"/><polygon points="14,11 77,5 140,11 148,20 148,60 140,69 77,75 14,69 6,60 6,20" fill="none" stroke="var(--green-border)" stroke-width="1"/></svg>
    <svg class="icon" viewBox="0 0 24 24"><circle cx="12" cy="12" r="9" fill="none" stroke="#fff" stroke-width="1.8"/></svg>
    <div class="label">4406 FOLLOWERS</div>
  </div>
</section>

<h2 class="welcome">Welcome To <span>Fieldhand</span></h2>
<p class="intro">Lorem ipsum dolor sit amet, consectetur adipiscing elit, sed do eiusmod tempor incididunt ut labore et dolore magna aliqua. Ut enim ad minim veniam, quis nostrud exercitation ullamco laboris nisi ut aliquip ex ea commodo consequat. Duis aute irure dolor in reprehenderit in voluptate velit esse cillum dolore eu fugiat nulla pariatur. Excepteur sint occaecat cupidatat non proident, sunt in culpa qui officia deserunt mollit anim id est laborum</p>

<article class="card" style="left:81px">
  <div class="card-title">Organic</div>
  <div class="card-photo photo-organic" role="img" aria-label="Wooden crate of fresh carrots and leafy greens"></div>
  <p class="card-text">Lorem ipsum dolor sit amet, consectetur adipiscing elit, sed do eiusmod tempor incididunt ut labore et dolore magna aliqua. Ut enim ad minim veniam,</p>
</article>
<article class="card" style="left:361px">
  <div class="card-title">Farm Fresh</div>
  <div class="card-photo photo-farm" role="img" aria-label="Ripe oranges hanging in a sunny orchard"></div>
  <p class="card-text">Lorem ipsum dolor sit amet, consectetur adipiscing elit, sed do eiusmod tempor incididunt ut labore et dolore magna aliqua. Ut enim ad minim veniam,</p>
</article>
<article class="card" style="left:641px">
  <div class="card-title">Meat</div>
  <div class="card-photo photo-meat" role="img" aria-label="Butcher counter with fresh cuts of meat and parsley"></div>
  <p class="card-text">Lorem ipsum dolor sit amet, consectetur adipiscing elit, sed do eiusmod tempor incididunt ut labore et dolore magna aliqua. Ut enim ad minim veniam,</p>
</article>

<footer class="footer">
  <h3 class="copy-head">COPYRIGHT</h3>
  <p class="copy-text">(c) 2016 fieldhand. All rights reserved.</p>
  <p class="footer-links">Home &nbsp;/&nbsp; About Us &nbsp;/&nbsp; How it works &nbsp;/&nbsp; Register &nbsp;/&nbsp; Contacts</p>
  <h3 class="addr-head">ADDRESS</h3>
  <p class="addr-text">48 Orchard Row, Larkfield, LK4 7PD</p>
  <p class="addr-phone">+1 800 555 0142</p>
  <h3 class="follow-head">FOLLOW US</h3>
  <span class="social" style="left:832px"></span>
  <span class="social" style="left:855px"></span>
  <span class="social" style="left:878px"></span>
</footer>

</body>
</html>
```